Purpose, Mission, and Values Poster Update

Corvane Field Laboratories, a Testing, Inspection, and Certification company in the Atlanta area, needs an updated PMV poster. Looking to update graphics and presentation, moving away from current design. Want to carry over company logo, colors (you can include additional blues in the design beyond what is mentioned in the brand guidelines as the previous design did), and messaging (see attachments).

We would also like a companion poster, using the same design language, that shows our goals for leads and won opportunities. Want to carry over logo, colors, and messaging from original, except for this one we want the leads goal to be 115 instead of 85.

Both posters need to be 6000w x 7200h at 300ppi, CMYK. We want to move away from the cartoony, corporate clipart sort of look that the current design has, as new leadership doesn't like the aesthetic.

Target Market(s)

Internal - group of engineers, chemists, scientists, and other technical personnel

Industry/Entity Type

TIC (Testing, Inspection, Certification)

Font styles to use
Serif
Sans Serif

Colors
0054AA
0677BA
7BADD7
CADEEF
E8F1F8

Requirements
Must have
• For both: CMYK colors for printing, 6000w x 7200h at 300ppi for poster sizing leads, company logo; for PMV poster: phrasing of purpose, mission, and values statements preserved; for ring the bell poster: leads goal updated to 115, opportunities goal unchanged at 25
Should not have
• Corporate clipart, cartoon characters

```html
<!DOCTYPE html>
<html lang="en">
<head>
<meta charset="utf-8">
<title>Corvane Field Laboratories – Purpose, Mission and Values</title>
<link href="https://fonts.googleapis.com/css2?family=Oswald:wght@500;600;700&family=Montserrat:wght@500;600&display=swap" rel="stylesheet">
<style>
  :root {
    --paper: #ffffff;
    --ink: #111111;
    --heading-grey: #6d6e73;
    --sky: #27a1dc;
    --navy: #0e5a92;
    --deep-blue: #0c5690;
    --mid-blue: #1a7bb6;
    --pale-blue: #e8f1f8;
    --icon-blue: #1f75b8;
  }
  * { margin: 0; padding: 0; box-sizing: border-box; }
  html, body { width: 1012px; height: 1200px; overflow: hidden; background: var(--paper); }
  .poster { position: relative; width: 1012px; height: 1200px; overflow: hidden; }

  /* Left panel */
  .intro { position: absolute; left: 0; top: 0; width: 484px; height: 1200px; background: var(--paper); }
  .brand { position: absolute; left: 90px; top: 150px; display: flex; align-items: center; gap: 12px; }
  .brand-mark { width: 30px; height: 30px; background: var(--ink); }
  .brand-name { font: 600 21px/1 "Montserrat", sans-serif; color: var(--ink); white-space: nowrap; }

  .timeline-line { position: absolute; left: 120px; top: 309px; width: 5px; height: 273px; background: var(--navy); }
  .timeline-node { position: absolute; left: 82px; width: 80px; height: 80px; border-radius: 50%;
    border: 5px solid var(--navy); background: var(--paper); display: flex; align-items: center; justify-content: center; }
  .timeline-node svg { width: 46px; height: 46px; }
  .node-purpose { top: 269px; }
  .node-mission { top: 542px; }

  .statement { position: absolute; left: 183px; width: 300px; }
  .statement-purpose { top: 238px; }
  .statement-mission { top: 510px; }
  .statement-kicker, .statement-title { display: block; transform: scaleX(0.89); transform-origin: left center; }
  .statement-kicker { font: 600 74px/1 "Oswald", sans-serif; color: var(--sky); }
  .statement-title { font: 600 74px/1.05 "Oswald", sans-serif; color: var(--heading-grey); }
  .statement-text { margin-top: 10px; font: 500 26px/31px "Montserrat", sans-serif; color: var(--ink); white-space: nowrap; }

  .team-photo { position: absolute; left: 0; top: 800px; width: 484px; height: 400px;
    background: linear-gradient(180deg, rgba(255,255,255,1) 0%, #e6ecf0 25%, #c9ced4 60%, #8d939b 100%); }

  /* Values band */
  .values-band { position: absolute; left: 484px; top: 0; width: 98px; height: 1200px; background: var(--sky);
    display: flex; flex-direction: column; align-items: center; padding-top: 62px; }
  .values-band span { font: 600 104px/115px "Oswald", sans-serif; color: #fff; text-shadow: 0 0 8px rgba(0,40,90,0.35); }

  /* Values list */
  .values { position: absolute; left: 582px; top: 0; width: 430px; height: 1200px;
    background: linear-gradient(90deg, var(--deep-blue) 0%, var(--mid-blue) 100%); }
  .value { position: absolute; left: 0; width: 430px; text-align: center; color: #fff; }
  .value-icon { width: 66px; height: 66px; margin: 0 auto; border-radius: 50%; background: #fff;
    box-shadow: 0 0 0 5px rgba(123,173,215,0.55); display: flex; align-items: center; justify-content: center; }
  .value-icon svg { width: 34px; height: 34px; }
  .value-title { margin-top: 10px; font: 600 34px/1.1 "Oswald", sans-serif; white-space: nowrap;
    transform: scaleX(0.82); transform-origin: center; }
  .value-text { margin-top: 6px; font: 500 19px/24px "Montserrat", sans-serif; color: var(--pale-blue); }
</style>
</head>
<body>
<main class="poster">
  <section class="intro">
    <div class="brand">
      <div class="brand-mark"></div>
      <div class="brand-name">Corvane Field Laboratories</div>
    </div>

    <div class="timeline-line"></div>
    <div class="timeline-node node-purpose">
      <svg viewBox="0 0 40 40" fill="none" stroke="#1f75b8" stroke-width="2.6" stroke-linecap="round">
        <circle cx="20" cy="15" r="8"/><circle cx="20" cy="15" r="3"/>
        <path d="M6 24 l6 8 h6 M34 24 l-6 8 h-6"/>
      </svg>
    </div>
    <div class="timeline-node node-mission">
      <svg viewBox="0 0 40 40" fill="none" stroke="#1f75b8" stroke-width="3" stroke-linecap="round">
        <circle cx="19" cy="21" r="14"/><circle cx="19" cy="21" r="7"/><circle cx="19" cy="21" r="1.5" fill="#1f75b8"/>
        <path d="M19 21 L33 7 M28 7 h5 v5"/>
      </svg>
    </div>

    <div class="statement statement-purpose">
      <span class="statement-kicker">OUR</span>
      <span class="statement-title">PURPOSE</span>
      <p class="statement-text">Create a safe &amp;<br>reliable world</p>
    </div>
    <div class="statement statement-mission">
      <span class="statement-kicker">OUR</span>
      <span class="statement-title">MISSION</span>
      <p class="statement-text">Deliver assurance<br>through precise<br>technical and<br>professional services</p>
    </div>

    <div class="team-photo" role="img" aria-label="Photo of two smiling colleagues in grey business suits seated at a desk in a bright office"></div>
  </section>

  <aside class="values-band" aria-label="Our values">
    <span>O</span><span>U</span><span>R</span><span>V</span><span>A</span><span>L</span><span>U</span><span>E</span><span>S</span>
  </aside>

  <section class="values">
    <div class="value" style="top:86px">
      <div class="value-icon"><svg viewBox="0 0 32 32" fill="#1f75b8"><circle cx="16" cy="10" r="4"/><circle cx="8" cy="14" r="3"/><circle cx="24" cy="14" r="3"/><path d="M10 26a6 6 0 0 1 12 0z M3 26a5 5 0 0 1 8-4v4z M29 26a5 5 0 0 0-8-4v4z"/></svg></div>
      <h2 class="value-title">KEEP PEOPLE FIRST</h2>
      <p class="value-text">Foster a collaborative &amp;<br>inclusive environment for<br>team members growth</p>
    </div>
    <div class="value" style="top:304px">
      <div class="value-icon"><svg viewBox="0 0 32 32" fill="none" stroke="#1f75b8" stroke-width="2.4" stroke-linecap="round"><circle cx="17" cy="10" r="6"/><path d="M14 10l2 2 4-4 M4 24h7l5 3 10-6"/></svg></div>
      <h2 class="value-title">DELIVER SERVICE EXCELLENCE</h2>
      <p class="value-text">Provide best-in-class<br>experiences for our clients</p>
    </div>
    <div class="value" style="top:497px">
      <div class="value-icon"><svg viewBox="0 0 32 32" fill="none" stroke="#1f75b8" stroke-width="2.4" stroke-linecap="round"><path d="M16 5a8 8 0 0 0-5 14v3h10v-3A8 8 0 0 0 16 5z M12 26h8"/></svg></div>
      <h2 class="value-title">THINK GLOBAL, ACT LOCAL</h2>
      <p class="value-text">Utilize our combined expertise<br>and knowledge to deliver<br>when and where</p>
    </div>
    <div class="value" style="top:713px">
      <div class="value-icon"><svg viewBox="0 0 32 32" fill="none" stroke="#1f75b8" stroke-width="2.4" stroke-linecap="round"><circle cx="17" cy="9" r="4"/><path d="M12 19a5 5 0 0 1 10 0 M4 24h7l5 3 10-6"/></svg></div>
      <h2 class="value-title">CREATE VALUE</h2>
      <p class="value-text">Work efficiently and effectively<br>to deliver quality results in<br>complex environments</p>
    </div>
    <div class="value" style="top:930px">
      <div class="value-icon"><svg viewBox="0 0 32 32" fill="none" stroke="#1f75b8" stroke-width="2.4" stroke-linecap="round"><circle cx="22" cy="9" r="5"/><path d="M19.5 9l2 2 3-3.5 M15 18h12 M15 23h12 M15 28h12"/><circle cx="7" cy="10" r="3"/><path d="M4 28v-9h6v9"/></svg></div>
      <h2 class="value-title">DO WHAT'S RIGHT</h2>
      <p class="value-text">Hold ourselves accountable to<br>the highest safety, professional<br>and personal standards</p>
    </div>
  </section>
</main>
</body>
</html>
```